Book Cover for Notes on the Quiet River's Far Lamps

I need a book cover for a 6 x 9 paperback titled Notes on the Quiet River's Far Lamps Gathered by Sailors and Weavers Resting in the Valley beyond the Northern Valley. It has to do with consciousness, the mind, incarnation onto Earth, leaving Earth, and the life in the life after this life. I have an idea I'm providing with this description, but I am open to anything that would be striking and stimulating, whether with a book or not. I am the author, T. Warren Blakely. I've added another background idea to see if anyone can do something with it and I've increased the budget.

```html
<!DOCTYPE html>
<html lang="en">
<head>
<meta charset="utf-8">
<title>Notes on the Quiet River's Far Lamps — Book Cover</title>
<link rel="stylesheet" href="https://fonts.googleapis.com/css2?family=Cinzel:wght@400;500&family=Marcellus&display=swap">
<style>
  :root {
    --backdrop: #e4e3e0;
    --leather-dark: #2a1a10;
    --leather-mid: #5a3a22;
    --leather-light: #8a6038;
    --frame-edge: #1c120b;
    --gold: #e8b818;
    --gold-deep: #7a5608;
    --brass: #a89040;
    --silver: #a9a9a6;
    --ornament: #b8922a;
  }
  * { margin: 0; padding: 0; box-sizing: border-box; }
  html, body { width: 1200px; height: 800px; overflow: hidden; }
  body { background: var(--backdrop); position: relative; }

  .cover {
    position: absolute; left: 345px; top: 25px; width: 510px; height: 750px;
    background: radial-gradient(ellipse at 50% 45%, var(--leather-light) 0%, var(--leather-mid) 45%, var(--leather-dark) 100%);
    border-radius: 3px;
  }
  .cover__frame {
    position: absolute; inset: 22px 30px 22px 24px;
    border: 3px solid var(--frame-edge);
    box-shadow: inset 0 0 0 10px rgba(40,24,12,.55), inset 0 0 0 12px rgba(150,100,50,.35);
  }
  .cover__panel {
    position: absolute; left: 92px; top: 77px; width: 326px; height: 591px;
    background: radial-gradient(ellipse at 50% 40%, #8f6a44 0%, #6a4a2c 50%, #3b2616 100%);
    border: 3px solid var(--frame-edge);
    box-shadow: 0 0 0 4px rgba(120,80,40,.6), 0 0 0 7px var(--frame-edge);
  }
  .stud {
    position: absolute; width: 44px; height: 44px; border-radius: 50%;
    background: radial-gradient(circle at 40% 35%, #d8cc80, var(--brass) 55%, #4e4216 100%);
  }
  .stud--tl { left: 26px; top: 23px; } .stud--tr { right: 24px; top: 23px; }
  .stud--bl { left: 26px; bottom: 20px; } .stud--br { right: 24px; bottom: 20px; }

  .clasp {
    position: absolute; left: 424px; top: 242px; width: 66px; height: 248px;
    background: linear-gradient(90deg, #6d6d6a, var(--silver) 50%, #6d6d6a);
    border-radius: 30px;
  }
  .corner { position: absolute; width: 46px; height: 46px; background: var(--ornament); opacity: .75; }
  .corner--tl { left: 100px; top: 86px; } .corner--tr { left: 364px; top: 86px; }
  .corner--bl { left: 100px; top: 612px; } .corner--br { left: 364px; top: 612px; }
  .key {
    position: absolute; left: 237px; top: 105px; width: 36px; height: 130px;
    background: linear-gradient(180deg, #a47a4a, #6f4e2c); border-radius: 14px;
  }

  .title-block { position: absolute; left: 92px; width: 326px; text-align: center; color: var(--gold);
    text-shadow: 0 1px 0 var(--gold-deep), 0 2px 3px rgba(0,0,0,.55); }
  .title-main { top: 238px; font-family: "Cinzel", serif; font-size: 58px; font-weight: 400; letter-spacing: 1px; line-height: 1; }
  .title-sub { top: 306px; font-family: "Marcellus", serif; font-size: 26px; line-height: 32px; }
  .divider { position: absolute; left: 122px; top: 397px; width: 266px; height: 2px; background: var(--gold); }
  .divider__mark { position: absolute; left: 236px; top: 389px; width: 38px; height: 16px; background: var(--gold); border-radius: 50%; }
  .title-tail { top: 418px; font-family: "Marcellus", serif; font-size: 23px; line-height: 32px; }
  .author { top: 605px; font-family: "Cinzel", serif; font-size: 28px; letter-spacing: 1px; }
</style>
</head>
<body>
  <main class="cover" aria-label="Book cover">
    <div class="cover__frame"></div>
    <div class="stud stud--tl" role="img" aria-label="Brass corner stud"></div>
    <div class="stud stud--tr" role="img" aria-label="Brass corner stud"></div>
    <div class="stud stud--bl" role="img" aria-label="Brass corner stud"></div>
    <div class="stud stud--br" role="img" aria-label="Brass corner stud"></div>
    <div class="cover__panel"></div>
    <div class="corner corner--tl" role="img" aria-label="Gold corner filigree"></div>
    <div class="corner corner--tr" role="img" aria-label="Gold corner filigree"></div>
    <div class="corner corner--bl" role="img" aria-label="Gold corner filigree"></div>
    <div class="corner corner--br" role="img" aria-label="Gold corner filigree"></div>
    <div class="key" role="img" aria-label="Antique bronze skeleton key"></div>

    <h1 class="title-block title-main">NOTES</h1>
    <p class="title-block title-sub">on the Quiet River's<br>Far Lamps Gathered by</p>
    <div class="divider"></div>
    <div class="divider__mark" role="img" aria-label="Small gold scroll ornament"></div>
    <p class="title-block title-tail">Sailors and Weavers Resting<br>in the Valley beyond the<br>Northern Valley.</p>
    <p class="title-block author">Author Name</p>

    <div class="clasp" role="img" aria-label="Ornate silver book clasp"></div>
  </main>
</body>
</html>
```